Marketing Flyer

I need a flyer for my marketing company. I would like for it to to be consistent with my logo and business card design. I would also like for there to be an image of a crowded waiting room, or restaurant with people gathered around a flat screen that reads "Your Ad Here".

• logo, info on attached doc.
• Possibly a picture people in a waiting room or restaurant with a digital sign present that reads "your ad here".

```html
<!DOCTYPE html>
<html lang="en">
<head>
<meta charset="utf-8">
<title>FieldLine Marketing Flyer</title>
<link href="https://fonts.googleapis.com/css2?family=Open+Sans:wght@400;600;700&family=Oswald:wght@500&display=swap" rel="stylesheet">
<style>
  :root {
    --canvas: #e6e4e2;
    --white: #ffffff;
    --ink: #111111;
    --grey-logo: #6d6e70;
    --green: #8dc63f;
    --dark-mid: #5b5755;
    --dark-edge: #3e3b39;
    --footer: #141414;
    --photo-wall: #c9cdc6;
    --photo-floor: #8a5a4a;
  }
  html, body {
    margin: 0;
    padding: 0;
    width: 1053px;
    height: 1200px;
    overflow: hidden;
    background: var(--canvas);
    font-family: "Open Sans", Arial, sans-serif;
  }
  .flyer {
    position: absolute;
    left: 65px;
    top: 2px;
    width: 788px;
    height: 1022px;
    background: var(--white);
    transform: scale(1.17);
    transform-origin: top left;
    overflow: hidden;
  }
  .benefits-panel {
    position: absolute;
    left: 0; top: 386px;
    width: 788px; height: 506px;
    background: radial-gradient(ellipse at 45% 35%, var(--dark-mid) 0%, var(--dark-edge) 75%);
  }
  .hero-art {
    position: absolute;
    left: 0; top: 0;
    width: 788px; height: 530px;
  }
  .brand {
    position: absolute;
    left: 25px; top: 84px;
    color: var(--grey-logo);
    font-weight: 700;
  }
  .brand-name {
    font-size: 46px;
    line-height: 1;
    letter-spacing: -1px;
  }
  .brand-sub {
    font-size: 16px;
    letter-spacing: 7px;
    margin-top: 4px;
  }
  .intro {
    position: absolute;
    left: 32px; top: 206px;
    width: 290px;
    color: var(--ink);
  }
  .intro h2 {
    margin: 0 0 12px;
    font-size: 17px;
    font-weight: 600;
  }
  .intro p {
    margin: 0;
    font-size: 16.5px;
    line-height: 24px;
  }
  .benefits-title {
    position: absolute;
    left: 0; top: 458px;
    width: 788px;
    margin: 0;
    text-align: center;
    font-family: "Oswald", "Arial Narrow", sans-serif;
    font-weight: 500;
    font-size: 31px;
    color: var(--green);
    letter-spacing: 0.2px;
  }
  .benefit {
    position: absolute;
    color: var(--white);
    font-size: 14.2px;
    line-height: 22px;
    padding-left: 32px;
    white-space: nowrap;
  }
  .benefit .tick {
    position: absolute;
    left: 0; top: 1px;
    width: 22px; height: 20px;
  }
  .benefit h3 {
    margin: 0;
    font-size: 14.2px;
    font-weight: 700;
    color: var(--green);
    line-height: 22px;
  }
  .benefit p { margin: 0; }
  .col-left { left: 31px; }
  .col-right { left: 391px; }
  .tagline {
    position: absolute;
    left: 0; top: 926px;
    width: 788px;
    text-align: center;
    font-size: 20px;
    color: var(--ink);
    margin: 0;
  }
  .footer-bar {
    position: absolute;
    left: 0; top: 988px;
    width: 788px; height: 34px;
    background: var(--footer);
    color: var(--white);
    font-size: 13px;
    letter-spacing: 0.3px;
  }
  .footer-bar span {
    position: absolute;
    top: 8px;
  }
  .footer-email { left: 26px; }
  .footer-web { left: 588px; }
  .phone-tab {
    position: absolute;
    left: 227px; top: 982px;
    width: 338px; height: 40px;
  }
  .phone-text {
    position: absolute;
    left: 0; top: 982px;
    width: 788px; height: 40px;
    display: flex;
    align-items: center;
    justify-content: center;
    gap: 12px;
    color: var(--white);
    font-size: 20px;
  }
</style>
</head>
<body>
  <div class="flyer">
    <div class="benefits-panel"></div>

    <svg class="hero-art" viewBox="0 0 788 530">
      <defs>
        <linearGradient id="photoTone" x1="0" y1="0" x2="0.4" y2="1">
          <stop offset="0" stop-color="var(--photo-wall)"/>
          <stop offset="0.45" stop-color="#b8bfc4"/>
          <stop offset="0.75" stop-color="#6f6a66"/>
          <stop offset="1" stop-color="var(--photo-floor)"/>
        </linearGradient>
      </defs>
      <g role="img" aria-label="Photo of a busy waiting room, people seated facing a wall screen showing 'Your Ad Here'">
        <polygon points="425,0 788,0 788,475 325,272" fill="url(#photoTone)"/>
      </g>
      <polygon points="788,475 788,520 700,475" fill="#2a1f1c"/>
      <line x1="419" y1="0" x2="343" y2="116" stroke="var(--green)" stroke-width="6"/>
      <line x1="397" y1="0" x2="342" y2="84" stroke="var(--green)" stroke-width="6"/>
      <line x1="343" y1="306" x2="530" y2="406" stroke="var(--green)" stroke-width="6"/>
    </svg>

    <div class="brand">
      <div class="brand-name">FieldLine</div>
      <div class="brand-sub">MARKETING</div>
    </div>

    <div class="intro">
      <h2>WHAT WE DO:</h2>
      <p>We design an ad for your company and place it on the TV at local businesses.</p>
    </div>

    <h1 class="benefits-title">BENEFITS OF ADVERTISING WITH FIELDLINE</h1>

    <div class="benefit col-left" style="top:534px">
      <svg class="tick" viewBox="0 0 22 20"><rect x="1.5" y="3.5" width="15" height="15" fill="none" stroke="#fff" stroke-width="2"/><path d="M5 10l4 4 11-12" fill="none" stroke="var(--green)" stroke-width="3"/></svg>
      <h3>INEXPENSIVE:</h3>
      <p>Only $31.00 per month!</p>
    </div>
    <div class="benefit col-left" style="top:601px">
      <svg class="tick" viewBox="0 0 22 20"><rect x="1.5" y="3.5" width="15" height="15" fill="none" stroke="#fff" stroke-width="2"/><path d="M5 10l4 4 11-12" fill="none" stroke="var(--green)" stroke-width="3"/></svg>
      <h3>EXPOSURE:</h3>
      <p>Our digital signage is placed in only the<br>best/high traffic businesses in your area.</p>
    </div>
    <div class="benefit col-left" style="top:690px">
      <svg class="tick" viewBox="0 0 22 20"><rect x="1.5" y="3.5" width="15" height="15" fill="none" stroke="#fff" stroke-width="2"/><path d="M5 10l4 4 11-12" fill="none" stroke="var(--green)" stroke-width="3"/></svg>
      <h3>REPETITION:</h3>
      <p>Your ad is shown over 3,500 time each<br>month (42,000 times per year)!</p>
    </div>
    <div class="benefit col-left" style="top:779px">
      <svg class="tick" viewBox="0 0 22 20"><rect x="1.5" y="3.5" width="15" height="15" fill="none" stroke="#fff" stroke-width="2"/><path d="M5 10l4 4 11-12" fill="none" stroke="var(--green)" stroke-width="3"/></svg>
      <h3>LOCAL:</h3>
      <p>We show your ad to consumers in YOUR area.<br>Let us help you do business with the people<br>you want to do business with.</p>
    </div>

    <div class="benefit col-right" style="top:534px">
      <svg class="tick" viewBox="0 0 22 20"><rect x="1.5" y="3.5" width="15" height="15" fill="none" stroke="#fff" stroke-width="2"/><path d="M5 10l4 4 11-12" fill="none" stroke="var(--green)" stroke-width="3"/></svg>
      <h3>EXCLUSIVITY:</h3>
      <p>Only 2 ads per industry.</p>
    </div>
    <div class="benefit col-right" style="top:601px">
      <svg class="tick" viewBox="0 0 22 20"><rect x="1.5" y="3.5" width="15" height="15" fill="none" stroke="#fff" stroke-width="2"/><path d="M5 10l4 4 11-12" fill="none" stroke="var(--green)" stroke-width="3"/></svg>
      <h3>LEAD GENERATION:</h3>
      <p>We show consumers how to reach you and<br>where to find you.</p>
    </div>
    <div class="benefit col-right" style="top:690px">
      <svg class="tick" viewBox="0 0 22 20"><rect x="1.5" y="3.5" width="15" height="15" fill="none" stroke="#fff" stroke-width="2"/><path d="M5 10l4 4 11-12" fill="none" stroke="var(--green)" stroke-width="3"/></svg>
      <h3>BRAND AWARENESS:</h3>
      <p>People need to know your business. We make<br>that happen by putting your brand right in<br>front of them.</p>
    </div>
    <div class="benefit col-right" style="top:801px">
      <svg class="tick" viewBox="0 0 22 20"><rect x="1.5" y="3.5" width="15" height="15" fill="none" stroke="#fff" stroke-width="2"/><path d="M5 10l4 4 11-12" fill="none" stroke="var(--green)" stroke-width="3"/></svg>
      <h3>DIGITAL:</h3>
      <p>Digital advertising has higher retention rates<br>and higher consumer engagement.</p>
    </div>

    <p class="tagline">Let us make you famous in your community!</p>

    <div class="footer-bar">
      <span class="footer-email">hello@fieldline-mail.com</span>
      <span class="footer-web">www.fieldline.com</span>
    </div>
    <svg class="phone-tab" viewBox="0 0 338 40" aria-hidden="true">
      <polygon points="14,0 320,0 338,40 0,40" fill="var(--green)"/>
    </svg>
    <div class="phone-text">
      <svg width="20" height="20" viewBox="0 0 20 20" aria-hidden="true">
        <circle cx="10" cy="10" r="8.5" fill="none" stroke="#fff" stroke-width="1.8"/>
        <path d="M7 5.5l1.6 2.6-1 1.2c.6 1.3 1.6 2.3 2.9 2.9l1.2-1 2.6 1.6-.8 1.6c-3.6.2-7.4-3.6-7.2-7.2z" fill="#fff"/>
      </svg>
      <span>+100 555 01420</span>
    </div>
  </div>
</body>
</html>
```